Dalvorn-Ke Photography needs a poster for a upcoming event

We need a Music Concert Poster designed for a musician named Marc T. Lindow. The concert is happening 6:30 pm, Saturday, January 10, 2015 Look to our current design ideas for inspiration. Keep it clean and simple but I want to see your creative ideas. Please view the throw togethers screenshots I have included in this project and then use one of the clean images in your design. Visit www.pinboardia.example/marclind/concert-posters/ for the musicians favorite music posters and gather ideas from there as well.

Industry/Entity Type

Event

Requirements
Nice to have
• Lets tend to lean towards a more sanserif font

```html
<!DOCTYPE html>
<html lang="en">
<head>
<meta charset="utf-8">
<title>Marc T. Lindow in Concert</title>
<link rel="stylesheet" href="https://fonts.googleapis.com/css2?family=Comfortaa:wght@300;400&family=Black+Ops+One&family=Special+Elite&family=Open+Sans:wght@400&display=swap">
<style>
  :root {
    --glow-yellow: #f7d21a;
    --glow-orange: #e9961a;
    --crowd-dark: #0c1408;
    --crowd-mid: #3b4a14;
    --banner-yellow: #fff23c;
    --ink-brown: #3b1c0e;
    --ink-dark: #1c1c18;
    --portrait-maroon: #3a1410;
    --portrait-purple: #5a2a86;
    --venue-red: #e0431d;
    --white: #ffffff;
  }
  * { margin: 0; padding: 0; box-sizing: border-box; }
  html, body { width: 1200px; height: 785px; overflow: hidden; background: var(--crowd-dark); }
  .poster { position: relative; width: 1200px; height: 785px; overflow: hidden; }

  .crowd-scene {
    position: absolute; inset: 0;
    background:
      radial-gradient(ellipse 620px 420px at 560px 170px, rgba(255,236,90,0.95), rgba(255,236,90,0) 70%),
      radial-gradient(ellipse 420px 300px at 1050px 260px, rgba(240,150,20,0.7), rgba(240,150,20,0) 70%),
      linear-gradient(to bottom, var(--glow-yellow) 0%, var(--glow-orange) 38%, var(--crowd-mid) 58%, var(--crowd-dark) 78%);
  }

  .date-block { position: absolute; left: 60px; top: 20px; width: 300px; height: 270px; }
  .date-block svg { position: absolute; inset: 0; }
  .event-time, .event-date {
    position: absolute; left: 38px;
    font-family: "Comfortaa", sans-serif; color: var(--ink-dark);
  }
  .event-time { top: 50px; font-size: 52px; font-weight: 300; letter-spacing: 1px; }
  .event-date { top: 118px; font-size: 27px; line-height: 36px; font-weight: 400; }
  .event-date sup { font-size: 16px; vertical-align: 12px; }
  .event-date .day-num { font-size: 38px; }

  .admission { position: absolute; left: 805px; top: 55px; }
  .admission-free, .admission-entrance {
    display: block; font-family: "Special Elite", sans-serif; text-transform: uppercase;
  }
  .admission-free { margin-left: 125px; font-size: 56px; color: var(--white); letter-spacing: 3px; line-height: 56px; }
  .admission-entrance { font-size: 46px; color: var(--ink-dark); letter-spacing: 2px; line-height: 46px; }
  .admission-key { position: absolute; left: 240px; top: 5px; }

  .portrait-frame {
    position: absolute; left: 358px; top: 62px; width: 478px; height: 478px;
    border-radius: 50%; background: var(--white);
  }
  .portrait-photo {
    position: absolute; left: 14px; top: 14px; width: 450px; height: 450px; border-radius: 50%;
    background: radial-gradient(circle at 55% 35%, #6b2a20 0%, var(--portrait-maroon) 45%, #1e0806 100%);
    overflow: hidden;
  }
  .portrait-photo::after {
    content: ""; position: absolute; left: 20px; top: 240px; width: 300px; height: 260px;
    border-radius: 45% 45% 0 0; background: var(--portrait-purple); opacity: 0.85;
  }

  .title-banner { position: absolute; left: 0; top: 0; width: 1200px; height: 785px; pointer-events: none; }
  .artist-name {
    position: absolute; left: 265px; top: 528px; width: 720px; text-align: center;
    font-family: "Black Ops One", sans-serif; font-size: 72px; color: var(--ink-brown);
    letter-spacing: 6px; transform: rotate(-1.8deg); text-transform: uppercase;
  }
  .concert-line {
    position: absolute; left: 430px; top: 612px;
    font-family: "Black Ops One", sans-serif; color: var(--ink-brown); transform: rotate(-1.8deg);
  }
  .concert-in { position: relative; display: inline-block; font-size: 26px; padding: 6px 12px; margin-right: 28px; vertical-align: middle; }
  .concert-in svg { position: absolute; left: -6px; top: -4px; }
  .concert-word { font-size: 52px; letter-spacing: 4px; vertical-align: middle; text-transform: uppercase; }

  .venue-box {
    position: absolute; left: 775px; top: 670px; width: 340px; height: 95px;
    background: var(--venue-red);
    clip-path: polygon(0 3%, 100% 0, 99% 76%, 1% 100%);
  }
  .venue-address {
    position: absolute; left: 775px; top: 680px; width: 340px; text-align: center;
    font-family: "Open Sans", sans-serif; font-size: 15px; line-height: 20px; color: var(--white);
    font-style: normal;
  }
</style>
</head>
<body>
<main class="poster">
  <div class="crowd-scene" role="img" aria-label="Concert crowd silhouettes with raised hands against bright yellow and orange stage lights"></div>

  <div class="date-block">
    <svg width="300" height="270" viewBox="0 0 300 270" aria-hidden="true">
      <path d="M10 100 C 30 40, 110 8, 230 12 C 120 16, 45 50, 10 100 Z" fill="var(--white)"/>
      <path d="M150 262 C 220 258, 270 215, 282 150 C 262 212, 215 250, 150 262 Z" fill="var(--white)"/>
    </svg>
    <p class="event-time">6.30Pm</p>
    <p class="event-date">Saturday<br>January <span class="day-num">10</span><sup>th</sup><br>2015</p>
  </div>

  <div class="admission">
    <span class="admission-free">Free</span>
    <span class="admission-entrance">Entrance</span>
    <svg class="admission-key" width="140" height="120" viewBox="0 0 140 120" aria-hidden="true">
      <line x1="50" y1="40" x2="112" y2="92" stroke="var(--white)" stroke-width="5"/>
      <line x1="70" y1="56" x2="84" y2="40" stroke="var(--white)" stroke-width="5"/>
      <line x1="82" y1="66" x2="94" y2="52" stroke="var(--white)" stroke-width="5"/>
      <circle cx="120" cy="98" r="11" fill="none" stroke="var(--white)" stroke-width="5"/>
    </svg>
  </div>

  <div class="portrait-frame">
    <div class="portrait-photo" role="img" aria-label="Portrait of the musician in a purple shirt holding a guitar over his shoulder"></div>
  </div>

  <svg class="title-banner" viewBox="0 0 1200 785" aria-hidden="true">
    <polygon points="205,512 1022,487 1005,660 222,700" fill="var(--banner-yellow)"/>
  </svg>
  <h1 class="artist-name">Marc T Lindow</h1>
  <p class="concert-line">
    <span class="concert-in">IN
      <svg width="80" height="48" viewBox="0 0 80 48" aria-hidden="true">
        <ellipse cx="28" cy="24" rx="26" ry="18" fill="none" stroke="var(--ink-brown)" stroke-width="2.5"/>
        <path d="M54 18 L76 18 M70 12 L76 18 L70 24" fill="none" stroke="var(--ink-brown)" stroke-width="2.5"/>
      </svg>
    </span><span class="concert-word">Concert</span>
  </p>

  <div class="venue-box"></div>
  <address class="venue-address">Harbor Glen Community Church,<br>482 Lantern Cove Rd,<br>Marlow Bay, FL, 32619</address>
</main>
</body>
</html>
```